Need Letterhead Design & Matching Business Card

I have a logo that I love already. But the letterhead is less than appealing and boring. I'd like a design for my letterhead which I will match with business cards. Also, I'd like to have used fonts that are generally available, as my current letterhead uses a font named "SPACE" which nobody has unless they download it...so when a Word version is forwarded, it looks awful on the receiver's screed due to not having the font. That being said, modern is the look we like and are going for.

My business is "Halloran Brightmoor PC" - a law firm specializing in representing people who have suffered catastrophic injuries or death (plane, auto, train crashes etc.).

See attached letterhead, which has all of the pertinent information. My logo is also attached in various formats.

```html
<!DOCTYPE html>
<html lang="en">
<head>
<meta charset="utf-8">
<title>Halloran Brightmoor PC — Stationery</title>
<link href="https://fonts.googleapis.com/css2?family=Arimo:wght@400&family=Tinos:wght@400&display=swap" rel="stylesheet">
<style>
  :root {
    --backdrop: #b3b3b3;
    --paper: #ffffff;
    --ink: #111111;
    --card-dark: #000000;
    --flap: #cccccc;
  }
  * { margin: 0; padding: 0; box-sizing: border-box; }
  html, body { width: 1200px; height: 1000px; overflow: hidden; }
  body { background: var(--backdrop); position: relative; font-family: 'Arimo', Arial, sans-serif; color: var(--ink); }
  .sheet { position: absolute; background: var(--paper); }

  .letterhead { left: 167px; top: 85px; width: 406px; height: 575px; }
  .cover { left: 627px; top: 85px; width: 406px; height: 575px; }
  .card-front { left: 58px; top: 686px; width: 185px; height: 110px; }
  .card-back { left: 58px; top: 802px; width: 185px; height: 111px; background: var(--card-dark); }
  .envelope-front { left: 266px; top: 693px; width: 426px; height: 213px; }
  .envelope-back { left: 715px; top: 693px; width: 426px; height: 213px; overflow: hidden; }

  .firm-name { position: absolute; white-space: nowrap; text-transform: uppercase; letter-spacing: 0.01em; font-weight: 400; }
  .firm-name .suffix { font-size: 0.55em; letter-spacing: 0; }

  .letterhead .firm-name { left: 50px; top: 51px; font-size: 12px; }
  .letterhead .contact { position: absolute; left: 290px; top: 24px; font-size: 7px; line-height: 9.1px; }

  .letter { position: absolute; left: 50px; top: 125px; width: 310px; font-family: 'Tinos', 'Times New Roman', serif; font-size: 7px; line-height: 8.6px; }
  .letter p { margin-bottom: 9px; }
  .letter .recipient { margin-top: 16px; margin-bottom: 15px; }
  .letter .signature { margin-top: 24px; }

  .cover .firm-name { left: 0; right: 0; top: 318px; text-align: center; font-size: 20px; }

  .card-front .firm-name { left: 16px; top: 22px; font-size: 9px; }
  .card-back .firm-name { left: 0; right: 0; top: 78px; text-align: center; font-size: 9px; color: var(--paper); }

  .envelope-front .firm-name { left: 19px; top: 23px; font-size: 10px; }
  .envelope-front .contact { position: absolute; left: 19px; top: 152px; font-size: 5.2px; line-height: 7.6px; }

  .envelope-back svg { position: absolute; left: 0; top: 0; }
</style>
</head>
<body>

  <section class="sheet letterhead">
    <div class="firm-name">Halloran Brightmoor <span class="suffix">PC</span></div>
    <address class="contact" style="font-style: normal;">
      R. Delano Whitcombe, Esq. | President<br>
      4120 Larkspur Ave. | suite 600<br>
      Fairmont Heights, CA 90418<br>
      delano@halloranbrightmoor.com<br>
      www.halloranbrightmoor.com<br>
      Tel: (855) 555-0192
    </address>
    <div class="letter">
      <p>Date</p>
      <p class="recipient">Recipient Name<br>Company Name<br>Street Address<br>City, State, ZIP</p>
      <p>Dear Name Here</p>
      <p>Typeset this letter in Times New Roman Regular 10 pt, on 12 pt. Leading. Dionsequis ad modiam il iure mod dolorper sustrud tet, velit veniatisi tetue vulluptatum adit nonsectem verat.</p>
      <p>Et lamet dolore dip ex cu feuis nit, conullutat atem quat. Rinum iriure dolorem dolorting elenisim zzriustionse ming ex eugue vullumsan henisit lor accum quis nos aloquis nosto cuissis cidunt loreet niamet wisi ex ero dolortinis exeratu mmolor secte dunt el ullaore rostie es feugiam vulluptatum zzriliquatin eseniam delenis ad eril estrud tet verat esto dolore feuisse niamconse venis accum nonsequat, cortisl iuscinis nullaorem veniamet, si. pis diam iliscin henis et iure tatueraessi.</p>
      <p>Andre tem ip eugiam alit, quat. Adiamet ad tat ulput wiscidui exeraessed tissit, quat nonumsan voleniat. um dolent parte magnismodio cor se min henim ipit ullumsandit vel iure do consequisl enisi. na commy nummy nibh etue vullut prat er susci et pratio dolore ming elit autem es feugiam dolorper incip et, con hendignibh exer at, quam do elit aliquat luptat. ut wis nullan ex el eum niam il dolore tetuer sisim nibh ex er aute ex et, quissequisl del ex et ad dolore tionse facili velenisim iliqui blam vel uatat, quisciliquis eriure min velit luptat venim vel ing etum ilit pratincin volorerostis non vercili quatio dolesed ea feuguer iuscin vent laor ilis dionseniam vel digna faci ex eros augait nosto dolore ero consecte elis autpat. dui blamet, vel ipit nullamcor in velestio euissim nostion ullamet, sequam, quat.</p>
      <p>Irit venim aut nibh eraestrud tio el euis nit ad magna feugue modipit lan ex et nonum dignibh exero odiam exeriure toe feugiamconse commod dolober senit dunt dolorem iriure dit erilit, commodi pismolent in ut wis adit, velis non utpat.</p>
      <p>Sincerely.</p>
      <p class="signature">Your Name Here<br>Title</p>
    </div>
  </section>

  <section class="sheet cover">
    <div class="firm-name">Halloran Brightmoor <span class="suffix">PC</span></div>
  </section>

  <section class="sheet card-front">
    <div class="firm-name">Halloran Brightmoor <span class="suffix">PC</span></div>
  </section>

  <section class="sheet card-back">
    <div class="firm-name">Halloran Brightmoor <span class="suffix">PC</span></div>
  </section>

  <section class="sheet envelope-front">
    <div class="firm-name">Halloran Brightmoor <span class="suffix">PC</span></div>
    <address class="contact" style="font-style: normal;">
      R. Delano Whitcombe, Esq. | President<br>
      4120 Larkspur Ave. | suite 600<br>
      Fairmont Heights, CA 90418<br>
      delano@halloranbrightmoor.com<br>
      www.halloranbrightmoor.com<br>
      Tel: (855) 555-0192
    </address>
  </section>

  <section class="sheet envelope-back">
    <svg width="426" height="213" viewBox="0 0 426 213" aria-hidden="true">
      <polygon class="envelope-flap" points="0,0 426,0 392,61 37,61" fill="var(--flap)"/>
    </svg>
  </section>

</body>
</html>
```